Business Card Design Project

Looking for a business card that our customers will remember. We are a high end Travel Agency.
Need a re-memorable classy business card.
Both sides full color.
Must have the following details.
Voyage Harbor Logo (see attached)
4B Wattle Lane
Penhurst Sydney NSW 2241
Phone: 02 9471 3652
Fax: 02 9563 4417
sales@voyageharbor-example.com.au
Consultant Name
Anything else you think we need

```html
<!DOCTYPE html>
<html lang="en">
<head>
<meta charset="utf-8">
<title>Voyage Harbor – Business Card</title>
<link rel="stylesheet" href="https://fonts.googleapis.com/css2?family=Ubuntu:wght@400;500;700&display=swap">
<style>
  :root {
    --stage: #2a2a2c;
    --teal-light: #4eaabf;
    --teal: #3a9ab2;
    --teal-deep: #2b869e;
    --map-tone: #6cbccd;
    --band: #f4f6f7;
    --band-shade: #d9e0e3;
    --brand-navy: #1c3358;
    --ink-light: #ffffff;
    --ink-soft: #dcecf1;
  }
  * { box-sizing: border-box; margin: 0; padding: 0; }
  html, body { width: 1200px; height: 900px; overflow: hidden; }
  body {
    background: var(--stage);
    font-family: "Ubuntu", Arial, sans-serif;
    position: relative;
  }
  .card {
    position: absolute;
    width: 560px;
    height: 320px;
    border-radius: 3px;
    overflow: hidden;
    background: linear-gradient(160deg, var(--teal-light) 0%, var(--teal) 55%, var(--teal-deep) 100%);
    box-shadow: 0 16px 40px rgba(0,0,0,0.55);
  }
  .card--back { left: 60px; top: 70px; }
  .card--front { left: 580px; top: 500px; }

  /* Back side */
  .world-map {
    position: absolute;
    left: 40px; top: 30px;
    width: 480px; height: 240px;
    border-radius: 40% 45% 40% 50%;
    background: radial-gradient(ellipse at 50% 45%, var(--map-tone) 0%, rgba(108,188,205,0.35) 55%, rgba(108,188,205,0) 75%);
  }
  .back-band {
    position: absolute;
    left: 0; top: 170px;
    width: 300px; height: 56px;
    background: linear-gradient(180deg, var(--band) 0%, var(--band-shade) 100%);
    display: flex; align-items: center; justify-content: center;
  }
  .website {
    position: absolute;
    right: 24px; bottom: 22px;
    color: var(--ink-soft);
    font-size: 14px;
    letter-spacing: 0.3px;
  }

  /* Brand name */
  .brand-name {
    font-family: "Ubuntu", Arial, sans-serif;
    font-weight: 500;
    color: var(--brand-navy);
    font-size: 24px;
    letter-spacing: 1px;
    white-space: nowrap;
  }

  /* Front side */
  .consultant {
    position: absolute;
    left: 34px; top: 40px;
    color: var(--ink-light);
  }
  .consultant__name { font-weight: 700; font-size: 24px; }
  .consultant__role { font-weight: 400; font-size: 18px; margin-top: 2px; color: var(--ink-soft); }

  .front-band {
    position: absolute;
    left: 0; top: 116px;
    width: 100%; height: 66px;
    background: linear-gradient(180deg, var(--band) 0%, var(--band-shade) 100%);
    display: flex; align-items: center; justify-content: flex-end;
    padding-right: 48px;
  }
  .contacts {
    position: absolute;
    left: 40px; top: 210px; right: 24px;
    display: flex; gap: 40px;
    color: var(--ink-soft);
    font-size: 15px;
  }
  .contacts__col { display: flex; flex-direction: column; gap: 14px; }
  .contact { display: flex; align-items: flex-start; gap: 12px; line-height: 1.3; }
  .contact svg { flex: none; width: 18px; height: 18px; margin-top: 1px; fill: var(--ink-soft); }
</style>
</head>
<body>

<section class="card card--back" aria-label="Card back">
  <div class="world-map" role="img" aria-label="Faint world map in light teal"></div>
  <div class="back-band"><span class="brand-name">Voyage Harbor</span></div>
  <p class="website">www.voyageharbor-example.com.au</p>
</section>

<section class="card card--front" aria-label="Card front">
  <div class="consultant">
    <p class="consultant__name">John Doe</p>
    <p class="consultant__role">Consultant</p>
  </div>
  <div class="front-band"><span class="brand-name">Voyage Harbor</span></div>
  <div class="contacts">
    <div class="contacts__col">
      <p class="contact">
        <svg viewBox="0 0 24 24" aria-hidden="true"><path d="M7 1h10a2 2 0 0 1 2 2v18a2 2 0 0 1-2 2H7a2 2 0 0 1-2-2V3a2 2 0 0 1 2-2zm0 3v14h10V4zm5 15.5a1.2 1.2 0 1 0 0 2.4 1.2 1.2 0 0 0 0-2.4z"/></svg>
        02 9471 3652
      </p>
      <p class="contact">
        <svg viewBox="0 0 24 24" aria-hidden="true"><path d="M6 2h12v6H6zM3 9h18a2 2 0 0 1 2 2v7h-4v4H5v-4H1v-7a2 2 0 0 1 2-2zm4 7v4h10v-4z"/></svg>
        02 9563 4417
      </p>
    </div>
    <div class="contacts__col">
      <p class="contact">
        <svg viewBox="0 0 24 24" aria-hidden="true"><path d="M2 5h20v14H2zm2 2v.4l8 5.6 8-5.6V7zm0 2.8V17h16V9.8l-8 5.6z"/></svg>
        sales@voyageharbor-example.com.au
      </p>
      <p class="contact">
        <svg viewBox="0 0 24 24" aria-hidden="true"><path d="M12 1a8 8 0 0 0-8 8c0 6 8 14 8 14s8-8 8-14a8 8 0 0 0-8-8zm0 11a3 3 0 1 1 0-6 3 3 0 0 1 0 6z"/></svg>
        <span>4B Wattle Lane<br>Penhurst Sydney NSW 2241</span>
      </p>
    </div>
  </div>
</section>

</body>
</html>
```